Lumavera Packaging Design Project Hair Removal products

Lumavera is launching a New Hair Removal Sub Brand, under the Lumavera Brand .

This new hair removal range will include approx six products that are all designed to remove hair. These include hot wax, wax strips, depilitaory creams, hair removal lotion etc.

We are looking for a fresh new look and a sub brand name for the range. Currently we have a name Lumavera Presto Glidea as a name option but we are not sold on this name so we would like to see other options . We would like the brand to use the same primary colours as our current lumavera brand. ie the pink and the blue but it should look different from the current range. I will email through all the pantones and logos on the brand. You can check out lumavera.co.za to see the current range

For the design we would like to see a design for a sticker that goes on a bottle as well as see how it translates on a box.

Target Market(s)

any female using hair removal products

Industry/Entity Type

Hair

Requirements
Must have
• simple design.

must use our colours

it must somehow portray that using our hair removal system is really quick, easy and effective

You can use images of legs on the packaging but it is not required.

all design must have the main brand logo "Lumavera" on the packaging but with regard to the sub name for the brand we are not sold on our name so we require that for one of your artwork options that you use our name "Presto Glidea" for one of the designs , however we would also like you to come up with your own name for the hair removal range.

Lumavera logo is not dominant and can remain in the background.

```html
<!DOCTYPE html>
<html lang="en">
<head>
<meta charset="utf-8">
<title>Lumavera Presto Glidea – Tube and Carton</title>
<link rel="stylesheet" href="https://fonts.googleapis.com/css2?family=Didact+Gothic&family=Open+Sans:wght@600&display=swap">
<style>
  :root {
    --pink: #e6397f;
    --pink-soft: #f7c3d8;
    --teal: #1b8aa8;
    --teal-soft: #bfe4ee;
    --line: #2b2b2b;
    --paper: #ffffff;
  }
  * { margin: 0; padding: 0; box-sizing: border-box; }
  html, body {
    width: 1200px; height: 1100px; overflow: hidden; background: var(--paper);
  }
  .artboard {
    position: relative; width: 960px; height: 880px;
    transform: scale(1.25); transform-origin: 0 0;
  }
  .dieline { position: absolute; left: 0; top: 0; }
  .dieline path, .dieline rect, .dieline polygon, .dieline line {
    fill: var(--paper); stroke: var(--line); stroke-width: 1;
  }
  .brand {
    position: absolute; width: 164px; text-align: center;
    font-family: "Didact Gothic", sans-serif; color: var(--pink);
  }
  .brand-name {
    display: flex; align-items: center; justify-content: center; gap: 6px;
    font-size: 25px; line-height: 1;
  }
  .brand-dot {
    width: 20px; height: 20px; border-radius: 50%; background: var(--pink);
  }
  .brand-tagline { font-size: 15px; margin-top: 6px; }
  .brand.is-flipped { transform: rotate(180deg); }
  .legs-art {
    position: absolute; border-radius: 40px;
    background: linear-gradient(180deg, var(--pink-soft) 0%, #fbe3ed 55%, var(--teal-soft) 100%);
  }
  .range-badge {
    position: absolute; border-radius: 14px; background: var(--pink);
    box-shadow: 0 0 4px 2px var(--pink-soft);
    color: #fff; font-family: "Open Sans", sans-serif; font-weight: 600;
    letter-spacing: 1px; display: flex; align-items: center; justify-content: center;
  }
  .copy {
    position: absolute; width: 156px; text-align: center;
    font-family: "Open Sans", sans-serif; font-weight: 600;
    font-size: 9px; line-height: 12px; color: var(--pink);
  }
  .copy p + p { margin-top: 14px; }
  .copy .lead { color: var(--teal); }
</style>
</head>
<body>
<div class="artboard">

  <svg class="dieline" width="960" height="880" viewBox="0 0 960 880" aria-hidden="true">
    <!-- tube -->
    <path d="M45 0 H208 Q220 0 220 12 L180 455 H42 L35 12 Q35 0 45 0 Z"/>
    <line x1="44" y1="14" x2="212" y2="14"/>
    <path d="M42 455 H178 V526 Q178 532 172 532 H48 Q42 532 42 526 Z"/>
    <!-- carton top lid -->
    <path d="M262 280 V100 Q262 88 274 88 H414 Q426 88 426 100 V280 Z"/>
    <line x1="262" y1="112" x2="426" y2="112"/>
    <!-- dust flaps -->
    <polygon points="426,280 432,262 432,166 552,166 584,262 590,280"/>
    <polygon points="754,280 760,262 790,166 912,166 912,262 918,280"/>
    <polygon points="426,684 432,712 462,798 584,798 584,700 590,684"/>
    <polygon points="754,684 760,700 760,798 884,798 912,712 918,684"/>
    <!-- bottom lid -->
    <path d="M590 684 H754 V866 Q754 876 744 876 H600 Q590 876 590 866 Z"/>
    <line x1="590" y1="848" x2="754" y2="848"/>
    <!-- glue flap -->
    <polygon points="918,280 958,292 958,672 918,684"/>
    <!-- body panels -->
    <rect x="262" y="280" width="164" height="404"/>
    <rect x="426" y="280" width="164" height="404"/>
    <rect x="590" y="280" width="164" height="404"/>
    <rect x="754" y="280" width="164" height="404"/>
  </svg>

  <!-- tube front -->
  <div class="brand" style="left:30px; top:48px;">
    <div class="brand-name">Lumavera <span class="brand-dot"></span></div>
    <div class="brand-tagline">Beauty from within</div>
  </div>
  <div class="legs-art" role="img" aria-label="Line drawing of two slender legs in high-heeled shoes" style="left:52px; top:158px; width:108px; height:176px;"></div>
  <div class="range-badge" style="left:47px; top:405px; width:125px; height:23px; font-size:12px;">Presto Glidea</div>

  <!-- carton top lid (upside down) -->
  <div class="brand is-flipped" style="left:262px; top:160px;">
    <div class="brand-name">Lumavera <span class="brand-dot"></span></div>
    <div class="brand-tagline">Beauty from within</div>
  </div>

  <!-- carton front panel -->
  <div class="brand" style="left:262px; top:308px;">
    <div class="brand-name">Lumavera <span class="brand-dot"></span></div>
    <div class="brand-tagline">Beauty from within</div>
  </div>
  <div class="legs-art" role="img" aria-label="Line drawing of two slender legs in high-heeled shoes" style="left:282px; top:420px; width:112px; height:176px;"></div>
  <div class="range-badge" style="left:270px; top:638px; width:146px; height:27px; font-size:14px;">Presto Glidea</div>

  <!-- carton side panel -->
  <div class="copy" style="left:430px; top:330px;">
    <p><span class="lead">more description here more</span> description here more descr iption here more description here more description here more description here mo re description here more des cription here more description here more description here mo re description here more descri ption here</p>
    <p><span class="lead">more description here more</span> description here more descr iption here more description here more description here more description here mo re description here more des cription here more description here more description here mo</p>
    <p><span class="lead">re description</span> here more descri ption here more description more description here more description here more description here</p>
  </div>

  <!-- carton back panel -->
  <div class="brand" style="left:590px; top:308px;">
    <div class="brand-name">Lumavera <span class="brand-dot"></span></div>
    <div class="brand-tagline">Beauty from within</div>
  </div>
  <div class="legs-art" role="img" aria-label="Line drawing of two slender legs in high-heeled shoes" style="left:610px; top:424px; width:112px; height:172px;"></div>
  <div class="range-badge" style="left:597px; top:641px; width:148px; height:27px; font-size:14px;">Presto Glidea</div>

  <!-- carton second side panel -->
  <div class="copy" style="left:758px; top:330px;">
    <p><span class="lead">more description here more</span> description here more descr iption here more description here more description here more description here mo re description here more des cription here more description here more description here mo re description here more descri ption here</p>
    <p><span class="lead">more description here more</span> description here more descr iption here more description here more description here more description here mo re description here more des cription here more description here more description here mo</p>
    <p><span class="lead">re description</span> here more descri ption here more description more description here more description here more description here</p>
  </div>

</div>
</body>
</html>
```